Legal firm website redesign

Existing site for Sydney CBD lawyer needs clean and professional redesign - http://penfoldlaw.com.au

The site will be viewed by a wide range of users: businesses, individuals, referral partners and other lawyers.

Please see the list of must haves for further details

Target Market(s)

Businesses, individuals, referral partners and other lawyers

Industry/Entity Type

Lawyer

Requirements
Must have
• Prominent display of phone number.
List of services down the left hand side of the site (5x services or so).
Search box in header.
Please use the greys and blues from the existing header.
New header must include the wording "Efficiency - Fulfillment - Integrity - Teamwork"

```html
<!DOCTYPE html>
<html lang="en">
<head>
<meta charset="utf-8">
<title>Penfold Law</title>
<link href="https://fonts.googleapis.com/css2?family=PT+Sans:wght@400;700&family=Arimo:wght@400&family=Crimson+Text:wght@700&display=swap" rel="stylesheet">
<style>
:root{
  --blue:#0b6db5;
  --blue-dark:#064f8c;
  --navy:#0a4a80;
  --grey-text:#555;
  --grey-mid:#888;
  --grey-line:#bbb;
  --footer:#2f2f2f;
  --white:#fff;
}
*{margin:0;padding:0;box-sizing:border-box}
html,body{width:1004px;height:1200px;overflow:hidden}
body{position:relative;background:linear-gradient(#f7f7f7,#e6e6e6 760px);font-family:"PT Sans",sans-serif;color:var(--grey-text)}
.abs{position:absolute}
.header{left:0;top:0;width:1004px;height:96px;background:repeating-linear-gradient(45deg,#e9e9e9 0 2px,#f1f1f1 2px 4px)}
.brand{left:90px;top:10px}
.brand-name{font-size:38px;font-weight:700;color:#555;letter-spacing:-.5px;line-height:40px}
.brand-url{font-family:Arimo,sans-serif;font-size:10px;color:#444;margin-left:9px;letter-spacing:.5px}
.nav{left:400px;top:0;width:510px;height:34px;border-bottom:1px solid var(--navy);display:flex;font-weight:700;font-size:13px;color:#444}
.nav a{text-decoration:none;color:inherit;padding-top:10px;text-align:center}
.nav .on{border-bottom:6px solid var(--navy);height:37px}
.phone{left:748px;top:44px;display:flex;align-items:center;gap:6px;font-size:21px;color:var(--blue-dark);font-weight:400}
.slider-frame{left:84px;top:78px;width:838px;height:349px;border-radius:16px;background:#f3f3f3;border:1px solid #ddd}
.slider-inner{left:107px;top:101px;width:793px;height:303px;border-radius:12px;background:#fff;box-shadow:0 0 6px #ccc}
.slide{left:118px;top:111px;width:771px;height:283px;border-radius:10px;background:linear-gradient(170deg,#2a2b2c 0%,#55544a 45%,#a8a37a 78%,#cfc9a0 100%)}
.slide-copy{left:151px;top:133px;width:560px;color:#fff}
.values{font-family:"Crimson Text",serif;font-size:25px;font-weight:700;padding-bottom:10px;border-bottom:1px dotted #999;word-spacing:3px}
.slide-copy p{font-size:11px;line-height:14px;margin-top:12px}
.btn{display:inline-block;margin-top:14px;background:#132c3f;border:1px solid #aab;padding:5px 9px;font-size:11px}
.arrow{top:237px;width:46px;height:40px;border-radius:8px;background:linear-gradient(#555,#222);box-shadow:0 3px 3px #999}
.dots{left:454px;top:386px;width:98px;height:26px;border-radius:13px;background:#f6f6f6;border:1px solid #ccc;display:flex;justify-content:center;align-items:center;gap:3px}
.dots i{width:10px;height:10px;border-radius:50%;background:#777}
.dots i:first-child{background:#fff;border:2px solid #888}
.section-title{font-size:30px;font-weight:700;line-height:32px}
.section-sub{font-size:10px;letter-spacing:4px;color:var(--grey-mid);margin:8px 0 0 22px}
.welcome{left:90px;top:448px}
.welcome .a{color:var(--blue)}
.rule{border-top:1px dotted #999}
.photo{left:74px;top:530px;width:129px;height:133px;background:#fff;border:1px solid #ddd;padding:5px}
.photo div{width:100%;height:100%;background:linear-gradient(#e8e4d8,#b99687 55%,#2b2f33)}
.intro{left:216px;top:530px;width:408px;font-family:Arimo,sans-serif;font-size:11.2px;line-height:16px;text-align:justify}
.intro ul{list-style:none;margin-left:13px;color:var(--blue);text-align:left}
.search{left:658px;top:435px;width:252px;height:51px;border:4px solid var(--blue);background:#fff;display:flex;align-items:center;padding:0 5px 0 10px}
.search span{flex:1;height:24px;border:1px solid #ddd;border-radius:12px 0 0 12px;font-family:Arimo,sans-serif;font-size:10px;color:#999;padding:6px 10px}
.search b{background:linear-gradient(#1a86d0,#0a5c9e);color:#fff;font-size:12px;padding:6px 7px}
.pubs{left:654px;top:490px;width:263px;height:326px;background:linear-gradient(#f0f0f0,#fff);box-shadow:0 0 4px #ccc}
.pubs h2{text-align:center;color:var(--blue);margin-top:10px}
.pubs .section-sub{text-align:center;margin:4px 0 0}
.pubs ul{list-style:none;margin:14px 14px 0;border-top:1px dotted #999;padding:10px 6px 0;font-family:Arimo,sans-serif;font-size:10.5px;line-height:14px;color:#555}
.pubs li{margin-bottom:14px}
.band{left:0;top:762px;width:1004px;height:315px;background:linear-gradient(var(--blue),#08528e)}
.areas{left:90px;top:775px;color:#fff}
.areas .section-sub{color:#cfe2f3;margin-left:6px}
.band-rule{left:74px;top:834px;width:855px;border-top:1px dotted #8ab4d8}
.col{top:862px;color:#fff}
.col h3{font-size:16px;font-weight:700;margin-bottom:16px}
.col ul{list-style:none;font-family:Arimo,sans-serif;font-size:11px;letter-spacing:.3px}
.col li{line-height:19.5px;padding-left:12px;position:relative}
.col li:before{content:"";position:absolute;left:2px;top:7px;border-left:4px solid #fff;border-top:3px solid transparent;border-bottom:3px solid transparent}
.divider{top:847px;height:210px;border-left:1px solid #4a8fce}
.footer{left:0;top:1077px;width:1004px;height:123px;background:var(--footer);color:#ddd;font-family:Arimo,sans-serif;font-size:11px;letter-spacing:.4px}
.foot-brand{position:absolute;left:74px;top:38px;font-family:"PT Sans",sans-serif;font-weight:700;font-size:32px;color:#aaa}
.foot-links{position:absolute;left:300px;top:46px;width:380px;text-align:center;line-height:18px}
.foot-contact{position:absolute;right:83px;top:36px;text-align:right;line-height:18px}
</style>
</head>
<body>
<div class="abs header"></div>
<div class="abs brand"><div class="brand-name">penfold law</div><div class="brand-url">www.penfoldlaw.com.au</div></div>
<nav class="abs nav">
  <a class="on" style="width:60px;margin-left:23px">HOME</a>
  <a style="width:100px">ABOUT US</a>
  <a style="width:110px">AREAS OF LAW</a>
  <a style="width:126px">PUBLICATIONS</a>
  <a style="width:70px">CONTACT</a>
</nav>
<div class="abs phone">
  <svg width="26" height="26" viewBox="0 0 26 26"><circle cx="13" cy="13" r="12" fill="#1f78c1"/><path d="M10 7h3l1 4-2 1q1 3 3 4l1-2 4 1v3q-7 1-10-11z" fill="#fff"/></svg>
  <span>(02) 9000 4821</span>
</div>

<div class="abs slider-frame"></div>
<div class="abs slider-inner"></div>
<div class="abs slide" role="img" aria-label="Photo of brass scales of justice against a cloudy sky"></div>
<div class="abs slide-copy">
  <div class="values">Efficiency &bull; Fulfillment &bull; Integrity &bull; Teamwork</div>
  <p>Penfold Law is a dynamic commercial law firm in the CBD of Sydney providing services to corporate, small business and private clients. Penfold Law brings together over 30 years of experience in legal practice. The strong focus of the firm is on commercial law and estate planning.</p>
  <p>Penfold Law is committed to providing quality legal services in helping its clients achieve their objectives by providing a proactive understanding of its clients' businesses and creative legal solutions.</p>
  <span class="btn">Read More &#9656;</span>
</div>
<div class="abs arrow" style="left:95px"><svg width="46" height="40"><path d="M19 13l7 7-7 7" stroke="#fff" stroke-width="4" fill="none"/></svg></div>
<div class="abs arrow" style="left:865px"><svg width="46" height="40"><path d="M27 13l-7 7 7 7" stroke="#fff" stroke-width="4" fill="none"/></svg></div>
<div class="abs dots"><i></i><i></i><i></i><i></i><i></i></div>

<div class="abs welcome">
  <h1 class="section-title"><span class="a">Welcome</span> Message</h1>
  <div class="section-sub">COMPANY INFORMATION</div>
</div>
<div class="abs rule" style="left:74px;top:512px;width:552px"></div>
<div class="abs photo"><div role="img" aria-label="Portrait photo of the founding director"></div></div>
<div class="abs intro">
  <p>Penfold Law commenced in September 2006 when Ray Penfold resigned from his significantly larger partnership to establish a boutique firm providing timely and cost effective services to corporate small business and private clients.</p><br>
  <p>Ray Penfold, the founding director of the firm, has for many years been involved at the cutting edge of the development of the legal professional in New South Wales. He is a:</p>
  <ul>
    <li>* member of the Elder Law &amp; Succession Committee of the State Law Society</li>
    <li>* director and past president of QP Inc (formerly Quality Practice Inc.)</li>
    <li>* past member of the Best Practice Committee of the State Law Society</li>
    <li>* member of Practice Standards Lawyers</li>
    <li>* Notary Public</li>
  </ul>
</div>

<div class="abs band"></div>
<div class="abs search"><span>Search Here............</span><b>Search</b></div>
<aside class="abs pubs">
  <h2 class="section-title">Publications</h2>
  <div class="section-sub">RECENT ADDITIONS</div>
  <ul>
    <li>Commencement of the Succession Act 2006 25.03.08</li>
    <li>Is that will valid? 15.01.08</li>
    <li>Labor's proposed changes to IR laws 14.12.07</li>
    <li>Should you make your own will? 14.11.07</li>
    <li>Illegal workers 14.08.07</li>
    <li>Employees' liability for misleading or deceptive conduct 14.08.07</li>
  </ul>
</aside>

<div class="abs areas">
  <h2 class="section-title">Areas of Law</h2>
  <div class="section-sub">LOCATION OF AREAS</div>
</div>
<div class="abs band-rule"></div>
<div class="abs col" style="left:90px">
  <h3>Commercial/Business Transactions</h3>
  <ul><li>Buying and selling businesses and companies</li><li>Financing</li><li>Leasing</li><li>Property transactions</li><li>Joint ventures</li><li>Business restructuring</li><li>Contract review and advice</li><li>Employment Law Documentation, e.g. AWAs</li></ul>
</div>
<div class="abs divider" style="left:388px"></div>
<div class="abs col" style="left:428px">
  <h3>Commercial Litigation</h3>
  <ul><li>Contesting wills</li><li>Intellectual property</li><li>Business disputes</li></ul>
</div>
<div class="abs divider" style="left:639px"></div>
<div class="abs col" style="left:684px">
  <h3>Estate Planning &amp; Succession</h3>
  <ul><li>Estate Planning</li><li>Simple wills</li><li>Tax effective wills</li><li>Asset protective wills</li><li>Enduring power of attorney</li><li>Appointment of enduring guardian</li><li>Special disability trusts</li><li>Administration of deceased estates</li></ul>
</div>

<footer class="abs footer">
  <div class="foot-brand">penfold law</div>
  <div class="foot-links">Home ~ About Us ~ Area of Law ~ Our People ~ Publication ~ Contact<br>Penfold Law, Copyright 2012-13, Privacy policy</div>
  <div class="foot-contact">Telephone (02) 9000 4821<br>Facsimile (02) 9000 4822<br>Email info@penfoldlaw.com.au</div>
</footer>
</body>
</html>
```